Orbit 528 - Pagevo Book Cover

I am looking for a Pagevo book cover for my book about "Orbit 528".
The Book is Titled:
Orbit 528 Advanced
Shaping Tomorrow: Paths Toward Unlocking Hidden Cosmic Laws
Author is Dorian Welby
Here is a book description that may help you understand more about it:
Inspired by the genius of Anton Brevik, this comprehensive guide delves into the ancient wisdom and cutting-edge science behind the 369 method, a powerful tool for manifesting your desires. Whether you're seeking personal growth, financial success, or spiritual enlightenment, this book provides advanced techniques and methods to transform your dreams into reality.
Any questions please ask.
Thanks
Colin

```html
<!DOCTYPE html>
<html lang="en">
<head>
<meta charset="utf-8">
<title>Orbit 528 Advanced – Book Cover</title>
<link rel="stylesheet" href="https://fonts.googleapis.com/css2?family=Montserrat:wght@700;800&family=Outfit:wght@400;500&display=swap">
<style>
  :root {
    --page-bg: #ffffff;
    --cover-deep: #0f0e1a;
    --cover-navy: #1b2450;
    --cover-violet: #5a2f6e;
    --glow-cyan: #8fe3f5;
    --numeral-blue: #8ed3ea;
    --title-white: #f4fbff;
    --tagline-cyan: #6fd3ea;
    --subtitle-pink: #f0b6f0;
    --author-white: #f2f2f5;
  }
  * { margin: 0; padding: 0; box-sizing: border-box; }
  html, body {
    width: 1200px;
    height: 1200px;
    overflow: hidden;
    background: var(--page-bg);
  }
  .book-cover {
    position: absolute;
    left: 240px;
    top: 60px;
    width: 720px;
    height: 1080px;
    background: var(--cover-deep);
    overflow: hidden;
  }
  .cosmic-art {
    position: absolute;
    left: 0; top: 0;
    width: 720px;
    height: 916px;
    background:
      radial-gradient(circle at 50% 42%, rgba(200, 240, 255, 0.9) 0%, rgba(170, 130, 220, 0.6) 10%, rgba(70, 80, 160, 0.4) 28%, transparent 55%),
      radial-gradient(ellipse at 85% 28%, rgba(150, 70, 150, 0.55) 0%, transparent 45%),
      radial-gradient(ellipse at 15% 55%, rgba(40, 70, 140, 0.55) 0%, transparent 50%),
      linear-gradient(180deg, #141632 0%, var(--cover-navy) 45%, #1a1a36 80%, var(--cover-deep) 100%);
  }
  .author-band {
    position: absolute;
    left: 0; top: 916px;
    width: 720px;
    height: 164px;
    background: var(--cover-deep);
  }
  .cover-text {
    position: absolute;
    left: 0;
    width: 720px;
    text-align: center;
  }
  .series-name {
    top: 148px;
    font-family: "Montserrat", sans-serif;
    font-weight: 800;
    font-size: 66px;
    letter-spacing: 3px;
    color: var(--title-white);
    text-shadow: 0 0 14px var(--glow-cyan), 0 0 4px var(--glow-cyan);
  }
  .series-number {
    top: 280px;
    font-family: "Montserrat", sans-serif;
    font-weight: 700;
    font-size: 300px;
    line-height: 1;
    letter-spacing: -6px;
    color: var(--numeral-blue);
    opacity: 0.88;
    text-shadow: 0 0 22px rgba(143, 227, 245, 0.8);
  }
  .edition-name {
    top: 628px;
    font-family: "Montserrat", sans-serif;
    font-weight: 800;
    font-size: 62px;
    letter-spacing: 2px;
    color: var(--title-white);
    text-shadow: 0 0 14px var(--glow-cyan), 0 0 4px var(--glow-cyan);
  }
  .tagline {
    top: 780px;
    font-family: "Montserrat", sans-serif;
    font-weight: 700;
    font-size: 22px;
    letter-spacing: 14px;
    padding-left: 14px;
    color: var(--tagline-cyan);
  }
  .subtitle {
    top: 876px;
    font-family: "Outfit", sans-serif;
    font-weight: 500;
    font-size: 21px;
    color: var(--subtitle-pink);
  }
  .author-name {
    top: 982px;
    font-family: "Outfit", sans-serif;
    font-weight: 500;
    font-size: 38px;
    letter-spacing: 2px;
    color: var(--author-white);
  }
</style>
</head>
<body>
  <main class="book-cover">
    <div class="cosmic-art" role="img" aria-label="Cosmic illustration: glowing light burst with sacred-geometry triangles, circles and radiating rays in blue and violet"></div>
    <div class="author-band"></div>

    <h1 class="cover-text series-name">ORBIT</h1>
    <div class="cover-text series-number">528</div>
    <div class="cover-text edition-name">ADVANCED</div>
    <p class="cover-text tagline">SHAPING TOMORROW</p>
    <p class="cover-text subtitle">Paths Toward Unlocking Hidden Cosmic Laws</p>
    <p class="cover-text author-name">DORIAN WELBY</p>
  </main>
</body>
</html>
```